Veltrona Cabinets Letter Head and Email Signature

Hi
I would love a design package for a letterhead, email signature, even update my business card if you like if you can come up with a great idea for my new high end cabinet shop. Veltrona Cabinets brings timeless craftsmanship to modern interiors, specializing in high end, custom cabinetry designed for architects and interior designers.

Target Market(s)

high end, luxury market

Industry/Entity Type

cabinet making

Requirements
Must have
• my colours of logo as the theme

```html
<!DOCTYPE html>
<html lang="en">
<head>
<meta charset="utf-8">
<title>Veltrona Cabinets – Letterhead and Email Signatures</title>
<link href="https://fonts.googleapis.com/css2?family=Lato:wght@400;700&family=Poppins:wght@300;400&family=Open+Sans:wght@600&display=swap" rel="stylesheet">
<style>
  :root {
    --backdrop: #979797;
    --paper: #ffffff;
    --brand-green: #4b7b4a;
    --ink: #3e3e3e;
    --body-grey: #5c5c5c;
    --label-ink: #1c1c1c;
    --divider: #8a8a8a;
    --signature-blue: #a9c3de;
  }
  * { margin: 0; padding: 0; box-sizing: border-box; }
  html, body { width: 1200px; height: 807px; overflow: hidden; }
  body { background: var(--backdrop); position: relative; font-family: "Lato", sans-serif; }

  .sheet { position: absolute; background: var(--paper); box-shadow: 0 2px 6px rgba(0,0,0,.25); }
  .sheet-label { position: absolute; font-family: "Open Sans", sans-serif; font-weight: 600; font-size: 13px; color: var(--label-ink); }

  .brand-name { position: absolute; color: var(--brand-green); font-weight: 400; white-space: nowrap; letter-spacing: .3px; }

  .contact-list { position: absolute; list-style: none; }
  .contact-list li { display: flex; align-items: center; white-space: nowrap; }
  .contact-list svg { flex: none; fill: var(--brand-green); }

  /* Letterhead */
  .letterhead { left: 55px; top: 50px; width: 477px; height: 674px; font-family: "Poppins", sans-serif; }
  .letterhead .brand-name { left: 44px; top: 36px; font-family: "Poppins", sans-serif; font-size: 18px; }
  .letterhead .contact-list { left: 315px; top: 39px; font-size: 7.4px; color: var(--ink); line-height: 10.4px; }
  .letterhead .contact-list svg { width: 7px; height: 7px; margin-right: 5px; }
  .salutation { position: absolute; left: 45px; top: 188px; font-size: 11.4px; font-weight: 300; color: var(--ink); }
  .letter-body { position: absolute; left: 45px; top: 224px; width: 392px; font-size: 6.5px; line-height: 10.2px; color: var(--body-grey); font-weight: 300; text-align: justify; }
  .letter-body p { margin-bottom: 10px; }
  .closing { position: absolute; left: 45px; top: 436px; font-size: 6.6px; color: var(--body-grey); font-weight: 300; }
  .signature-area { position: absolute; left: 41px; top: 466px; width: 84px; height: 35px; background: linear-gradient(90deg, var(--signature-blue), #c9d8ea); opacity: .55; border-radius: 3px; }

  /* Email signatures */
  .signature-wide { left: 581px; top: 116px; width: 529px; height: 202px; }
  .signature-wide .brand-name { left: 50px; top: 86px; font-size: 21px; }
  .signature-wide .divider { position: absolute; left: 263px; top: 53px; width: 1px; height: 110px; background: var(--divider); }
  .person-name { position: absolute; color: var(--brand-green); font-weight: 700; font-size: 21px; white-space: nowrap; }
  .person-role { position: absolute; color: var(--ink); font-size: 13px; white-space: nowrap; }
  .signature-wide .person-name { left: 281px; top: 47px; }
  .signature-wide .person-role { left: 281px; top: 74px; }
  .signature-wide .contact-list { left: 278px; top: 103px; font-size: 13.2px; color: var(--ink); line-height: 16.4px; }
  .email-sig .contact-list svg { width: 11px; height: 11px; margin-right: 8px; }

  .signature-tall { left: 581px; top: 380px; width: 269px; height: 325px; }
  .signature-tall .brand-name { left: 38px; top: 52px; font-size: 21px; }
  .signature-tall .person-name { left: 34px; top: 141px; }
  .signature-tall .person-role { left: 34px; top: 168px; }
  .signature-tall .contact-list { left: 31px; top: 216px; font-size: 13.2px; color: var(--ink); line-height: 16.4px; }
</style>
</head>
<body>

<svg width="0" height="0" style="position:absolute" aria-hidden="true">
  <defs>
    <symbol id="icon-phone" viewBox="0 0 16 16"><path d="M3.5 1.5 6 1l1.5 3.5-1.8 1.3a9 9 0 0 0 4.5 4.5l1.3-1.8L15 10l-.5 2.5c-.3 1.2-1.4 2-2.6 1.8C6.700 13.400 2.600 9.300 1.700 4.100 1.500 2.900 2.300 1.800 3.500 1.500Z"/></symbol>
    <symbol id="icon-mail" viewBox="0 0 16 16"><path d="M1 3h14v10H1z M2 4.2v.6l6 4 6-4v-.6Z" fill-rule="evenodd"/></symbol>
    <symbol id="icon-globe" viewBox="0 0 16 16"><path d="M8 1a7 7 0 1 0 0 14A7 7 0 0 0 8 1Zm-1 2.5 1.5 1-1 2L5 7 4 5.5Zm3 3 2.5 1L12 11l-2 1-1-2.5Z" fill-rule="evenodd"/></symbol>
  </defs>
</svg>

<section class="sheet letterhead" aria-label="Letterhead">
  <div class="brand-name">Veltrona Cabinets</div>
  <ul class="contact-list">
    <li><svg><use href="#icon-phone"/></svg>0412558390</li>
    <li><svg><use href="#icon-mail"/></svg>info@veltronacabinets.com.au</li>
    <li><svg><use href="#icon-globe"/></svg>www.veltronacabinets.com.au</li>
  </ul>

  <p class="salutation">Dear Mr. Harlow,</p>
  <div class="letter-body">
    <p>Lorem ipsum dolor sit amet, consectetur adipiscing elit. Donec orci purus, luctus vitae dignissim eu, iaculis sed purus. Vivamus faucibus, ipsum nec aliquet viverra, leo mauris condimentum ligula, sit amet sagittis enim ligula quis arcu. Nam egestas tortor id nisi porttitor mattis. In tortor ante, ultricies in suscipit a, tempus non massa. Vivamus et auctor mi. Fusce vel massa nulla. Phasellus nec eros mauris, et scelerisque orci.</p>
    <p>Donec malesuada orci vitae nulla accumsan porta a id massa. Quisque accumsan iaculis magna sit amet fringilla. Maecenas consequat, magna eget tincidunt semper, odio nibh rutrum mi, id feugiat ante nisi eu risus. Vestibulum nunc orci, rhoncus a placerat in, ultricies in mi. Cras mattis varius eros, vel fringilla nisi suscipit eget. Quisque scelerisque sagittis nulla at porttitor.</p>
    <p>Sed id augue vitae urna euismod commodo aliquet a quam. Pellentesque arcu velit, cursus et malesuada ut, consequat et diam. Nullam erat sem, rhoncus id ullamcorper vitae, rhoncus et arcu. In ultricies ultricies nulla, ut rutrum nisi iaculis at. Donec eu magna a metus ornare faucibus. Fusce aliquet faucibus ultricies. Morbi semper, est id tincidunt gravida, sem arcu adipiscing lacus, ac bibendum nulla leo eu purus. Quisque nec diam sed risus consectetur a accumsan quis quis nibh. Vestibulum id purus lorem.</p>
    <p>It is a long established fact that a reader will be distracted by the readable content of a page when looking at its layout. The point of using Lorem Ipsum is that it has a more-or-less normal distribution of letters, as opposed to using 'Content here, content here', making it look like readable English. Many desktop publishing packages</p>
  </div>
  <p class="closing">Sincerely,</p>
  <div class="signature-area" role="img" aria-label="Handwritten signature of Daniel Harlow"></div>
</section>
<p class="sheet-label" style="left:243px; top:729px;">Letterhead</p>

<section class="sheet email-sig signature-wide" aria-label="Email signature, horizontal">
  <div class="brand-name">Veltrona Cabinets</div>
  <div class="divider"></div>
  <p class="person-name">Marcus Elleray</p>
  <p class="person-role">Director Craftsman</p>
  <ul class="contact-list">
    <li><svg><use href="#icon-phone"/></svg>0412558390</li>
    <li><svg><use href="#icon-mail"/></svg>info@veltronacabinets.com.au</li>
    <li><svg><use href="#icon-globe"/></svg>www.veltronacabinets.com.au</li>
  </ul>
</section>
<p class="sheet-label" style="left:781px; top:331px;">Email Signature 1</p>

<section class="sheet email-sig signature-tall" aria-label="Email signature, stacked">
  <div class="brand-name">Veltrona Cabinets</div>
  <p class="person-name">Marcus Elleray</p>
  <p class="person-role">Director Craftsman</p>
  <ul class="contact-list">
    <li><svg><use href="#icon-phone"/></svg>0412558390</li>
    <li><svg><use href="#icon-mail"/></svg>info@veltronacabinets.com.au</li>
    <li><svg><use href="#icon-globe"/></svg>www.veltronacabinets.com.au</li>
  </ul>
</section>
<p class="sheet-label" style="left:609px; top:722px;">Email Signature 2</p>

</body>
</html>
```